Medical software helping patients with dry eye disease needs a business card

We have a logo we just need a design for a business card for a Canadian company called LOV: Dry Eye. We use AI technology to assist optometrists in properly diagnosing patients with dry eye disease reducing wait times in doctors offices and accuracy of diagnosis as well as identifying key possible indicators and tailored treatment plans. The final design should be clean and medical looking. Our mission is to help patients and our logo using blues and whites.

```html
<!DOCTYPE html>
<html lang="en">
<head>
<meta charset="utf-8">
<title>LOV: Dry Eye – Business Card</title>
<link rel="stylesheet" href="https://fonts.googleapis.com/css2?family=Cinzel:wght@600&family=Poppins:wght@400;500&display=swap">
<style>
  :root {
    --navy: #02436b;
    --cyan: #62c8d8;
    --white: #ffffff;
    --page: #eef1f4;
    --disc-light: #f7f7f8;
    --disc-mid: #e4e4e8;
    --disc-edge: #cfd0d6;
  }
  * { margin: 0; padding: 0; box-sizing: border-box; }
  html, body {
    width: 1200px; height: 900px; overflow: hidden;
    background: var(--page);
  }
  .business-card {
    position: absolute; left: 100px; top: 140px;
    width: 1000px; height: 619px;
    background: var(--cyan);
    overflow: hidden;
    box-shadow: 0 14px 40px rgba(2, 67, 107, 0.18);
    font-family: "Poppins", sans-serif;
    color: var(--white);
  }
  .navy-panel {
    position: absolute; left: 0; top: 0;
    width: 680px; height: 100%;
    background: var(--navy);
  }
  .brand-disc {
    position: absolute;
    left: 414px; top: 43px;
    width: 532px; height: 532px;
    border-radius: 50%;
    background: radial-gradient(circle at 42% 38%, var(--disc-light) 0%, var(--disc-mid) 62%, var(--disc-edge) 100%);
    display: flex; align-items: center; justify-content: center;
  }
  .brand-name {
    font-family: "Poppins", sans-serif;
    font-weight: 500;
    font-size: 58px;
    letter-spacing: 1px;
    color: var(--navy);
    white-space: nowrap;
  }
  .person {
    position: absolute; left: 60px; top: 62px;
  }
  .person-name {
    font-family: "Cinzel", serif;
    font-weight: 600;
    font-size: 47px;
    line-height: 1;
    letter-spacing: 1px;
  }
  .person-title {
    font-size: 29px;
    line-height: 1.2;
    margin-top: 4px;
  }
  .address {
    position: absolute; left: 60px; top: 254px;
    font-size: 28px; line-height: 36px;
    font-style: normal;
  }
  .contacts {
    position: absolute; left: 60px; top: 450px;
    list-style: none;
    font-size: 29px; line-height: 36.5px;
  }
  .contacts li { display: flex; align-items: center; gap: 9px; }
  .contact-icon { width: 26px; height: 26px; flex: none; }
</style>
</head>
<body>
  <div class="business-card">
    <div class="navy-panel"></div>

    <div class="brand-disc">
      <span class="brand-name">LOV: Dry Eye</span>
    </div>

    <div class="person">
      <h1 class="person-name">John Smith</h1>
      <p class="person-title">Managing Director</p>
    </div>

    <address class="address">
      421, Address line<br>
      goes here address<br>
      45452, Country
    </address>

    <ul class="contacts">
      <li>
        <svg class="contact-icon" viewBox="0 0 24 24" aria-hidden="true">
          <path fill="#fff" d="M6.6 10.8a15.1 15.1 0 0 0 6.6 6.6l2.2-2.2a1 1 0 0 1 1-.25 11.4 11.4 0 0 0 3.6.6 1 1 0 0 1 1 1V20a1 1 0 0 1-1 1A17 17 0 0 1 3 4a1 1 0 0 1 1-1h3.5a1 1 0 0 1 1 1c0 1.25.2 2.45.6 3.6a1 1 0 0 1-.25 1z"/>
          <path fill="none" stroke="#fff" stroke-width="1.8" stroke-linecap="round" d="M14 3.5a7 7 0 0 1 6.5 6.5M14 7a3.5 3.5 0 0 1 3 3"/>
        </svg>
        044-123 456 789
      </li>
      <li>
        <svg class="contact-icon" viewBox="0 0 24 24" aria-hidden="true">
          <rect x="2" y="5" width="20" height="14" fill="#fff"/>
          <path d="M2.5 5.5 12 13l9.5-7.5M2.5 18.5l7-6.5M21.5 18.5l-7-6.5" fill="none" stroke="#02436b" stroke-width="1.4"/>
        </svg>
        info@webname.com
      </li>
      <li>
        <svg class="contact-icon" viewBox="0 0 24 24" aria-hidden="true">
          <g fill="none" stroke="#fff" stroke-width="1.8">
            <circle cx="12" cy="12" r="10"/>
            <ellipse cx="12" cy="12" rx="4.5" ry="10"/>
            <path d="M2 12h20M4 6.5h16M4 17.5h16"/>
          </g>
        </svg>
        www.websitename.com
      </li>
    </ul>
  </div>
</body>
</html>
```